Website design targeting software developers who need to create better software, faster

Our website design and content will reflect that:
We created TernVantage to EMPOWER developers and their companies to create better software, faster and with less sweat!
The first solution of its kind, TernVantage provides software developers, team leaders and executives with the world’s only Keystroke Yield Metrics that helps them create better quality code, faster. It’s a breakthrough in coding development and lifestyle, and our website should reflect this.
A strong analogy for TernVantage is like vision goggles for developers. Developers have full visibility of their coding effort, past and present, and receive ongoing feedback on where, when, and how much coding effort they are delivering into the codebase. This keeps them on the right path and aware of where their code is impacting colleagues, or being impacted by them. The same applies to the team leader and executives. TernVantage simply provides them with the management view of their teams activity and progress to empower them to make more objective, accurate and timely decisions.
This website should therefore reflect this “individual night vision goggles” benefit, in addition to the teamwork that this world-first service facilitates.
TernVantage is also a very smart system that learns every developer’s, team’s and company’s past experience, and pro-actively alerts individuals and teams to avoid pit-falls and optimize processes based on their own previous projects, and that of colleagues. The website design should therefore reflect this smart, learning and collaborative environment.
Website structure:
The website is structured to clearly demonstrate this unique value with separate pages drilling down to present the benefits:
1. throughout the development team from individual developers to team leaders and executives (one section, 3 pages, 5 mini tabs within each page)
2. throughout the development cycle from project planning to coding, quality control and production (one section, 4 pages)
The website also includes some important informational pages such as pricing plans, About TernVantage, a ‘featured integrations’ page and a ‘technology’ page.
That is, home page + 5 inside page templates plus three icons
• “Home”
o Including animated counter of source code commits benchmarked through Keystroke Yield MetricsTM.
o Includes graphics illustrating the benefits of Pilot Signals.
• “Product” template
o Developer page (with 5 tabs: planning, coding, quality, production, outsourcing)
o Team leader page (with same 5 tabs)
o Executive page (with same 5 tabs)
• About & technology template - mainly text
o About may include inspirational image with working/happy developers
o Technology – may include supporting diagram image
• Plans & pricing template (a simple presentation of price plan alternatives)
• Featured integrations template (a visual display of recognized logos with short text)
• Blog – with landing page and inside post page. Including standard blog functionality – comments, share, author/date, etc. This should be suitable for use as a Postmill.example template
• Three Pilot Signal icons
The bottom line for our audience, and therefore our website, is this: We believe that for software developers, Return on Effort is the new Return on Investment because software developers are a key asset for any company.
The theme for our website is therefore: EMPOWERING developers and their companies to create better code, faster and with less sweat.
Delivery notes:
NOTE 1) THE ATTACHED PDF IS A CONTENT GUIDE ONLY – IT IS NOT A STYLE GUIDE NOR A LAYOUT GUIDE. The designer has free reign over matters of style and layout.
NOTE 2) Various logos are attached for usage in graphic creation.
NOTE 3) The site will be ultimately coded into Liferay a template, theme, and CSS. Competitors are welcome to quote for the work to carry out this coding and to incorporate the copy provided by TernVantage.
-
Example pages
-
Home Page=> http://ternvantage.pageloft.example/ternvantage
Developer-Planning=> http://ternvantage.pageloft.example/ternvantage#!developers-coding/c1og4
Developer-Coding=> http://ternvantage.pageloft.example/ternvantage#!developer-coding/c1mcz
Integrations=> http://ternvantage.pageloft.example/ternvantage#!featured-integrations/cvsy
Integrations-Taskhub=> http://ternvantage.pageloft.example/ternvantage#!integration-kelvory-taskhub/c2549
Plans & Pricing=> http://ternvantage.pageloft.example/ternvantage#!plans-pricing/cjcc
About=> http://ternvantage.pageloft.example/ternvantage#!about/ccjb
About-Technology=> http://ternvantage.pageloft.example/ternvantage#!about-technology/czvv
About-Services=> http://ternvantage.pageloft.example/ternvantage#!about-services/c1lrx
Updates
We note that a business that has had remarkable success with their positioning and design in a related market segment to TernVantage is Haldane Gauge. Their website can be found here:
Please ensure that the home page has a logo for an introductory video to be displayed. This video is currently under development and will be available for the new web-site launch.
Reason: Based on feedback we have extended the competition by 48 hours. Thanks for your submissions so far!
Reason: Deadline extended by one more day as per one teams request. This takes us to the end of the week and there will be no further extensions of the deadline. We are currently deliberating on first and second place.
Target Market(s)
TernVantage targets software developers, team leaders and executives at software developing companies.
Industry/Entity Type
Software
Requirements
Must have
- A very human feel! Developers at work, not play, but clearly happy, focused, in control of their domain, empowered with the tools and ‘visibility’ they need to get their job done well, on time and on budget.
We created our technology for developers, empowering them as individuals and valued assets to any company. Therefore inside the targeted sections of the website (see website structure notes above) we should therefore see them, their faces, and look into the eyes of developers, team leaders and executives.
TernVantage logo.
Upper tool bar – with these tabs:
• Product
• Plans & Pricing
• Blog
Full site map at the bottom of every page to facilitate easy navigation throughout the website.
• Product
o Developers
o Team Leaders
o Executives
o Services
o Featured Integrations
• Plans & Pricing
• About
o Why TernVantage
o Technology
o Contact
• Blog
Nice to have
- Icons in one strong theme throughout the website, for all the elements we discuss – including throughout the development cycle (planning, development, quality, production, outsourcing) and the pricing plans.
The analogy of night vision goggles (personal, agile tool providing vision to the otherwise dark domain) may or may not work well.
Should not have
- Should not have a dark theme; we are bringing software development out of the dark, into the light.
Should not have pages with crowded text or pages with only text; all pages should have some visual / image component.

```html
<!DOCTYPE html>
<html lang="en">
<head>
<meta charset="utf-8">
<title>TernVantage — better software, less sweat</title>
<link href="https://fonts.googleapis.com/css2?family=Open+Sans:wght@400;600;700&family=Oswald:wght@600&display=swap" rel="stylesheet">
<style>
:root{
  --navy:#0f1560;
  --navy-deep:#0a0f4a;
  --royal:#1f4fc4;
  --sky:#cfe3f7;
  --pale:#eaf3fc;
  --green:#5fb81c;
  --ink:#222;
  --grey:#8a8a8a;
  --footer:#d3d3d3;
  --line:#c9d3e0;
}
*{box-sizing:border-box;margin:0;padding:0}
html,body{width:819px;height:1200px;overflow:hidden}
body{position:relative;font-family:"Open Sans",Arial,sans-serif;color:var(--ink);background:#fff}
.abs{position:absolute}

/* header */
.site-header{left:0;top:0;width:819px;height:66px;background:linear-gradient(#f7fbff,#dfeefb)}
.brand{display:flex;align-items:center;gap:7px;font-weight:700;font-size:25px;color:var(--navy);letter-spacing:-.3px}
.brand-mark{width:22px;height:22px;background:var(--navy)}
.header-brand{left:37px;top:26px}
.tagline{left:349px;top:30px;font-size:19px;color:var(--navy)}
.tagline b{color:#000;font-weight:600;margin-left:10px}
.free{left:626px;top:20px;font-style:italic;font-size:15px;color:#333}
.cta{left:673px;top:28px;width:111px;height:27px;border-radius:4px;background:linear-gradient(#3b8be6,#1a5fd0);color:#fff;font-family:"Oswald",Impact,sans-serif;font-size:18px;text-align:center;line-height:27px;letter-spacing:.5px}

/* nav */
.main-nav{left:0;top:66px;width:819px;height:31px;background:var(--navy-deep);display:flex}
.main-nav a{color:#fff;font-size:12px;text-decoration:none;padding:0 22px;line-height:31px;border-right:1px solid #2a3080}
.main-nav a.active{color:#7fb0ff}
.main-nav a.drop::after{content:" ▾";font-size:9px;color:#8aa}
.sign-in{left:741px;top:69px;width:55px;height:25px;background:var(--green);color:#fff;font-size:11px;text-align:center;line-height:25px}

/* hero */
.hero{left:0;top:97px;width:819px;height:290px;background:linear-gradient(100deg,#fdfeff 0%,#c8daf1 28%,#4f82d4 52%,#3570d0 75%,#2a64c9 100%)}
.hero-photo{left:95px;top:133px;width:290px;height:254px;background:linear-gradient(160deg,rgba(245,249,255,.95),rgba(170,192,222,.75) 60%,rgba(70,85,110,.55));border-radius:10px 10px 0 0}
.hero-copy{left:427px;top:186px;width:300px;color:#fff;font-size:12.5px;line-height:17px;text-shadow:0 1px 2px rgba(10,20,70,.45)}
.arrow{width:34px;height:34px;border-radius:50%;background:rgba(120,140,170,.35)}
.arrow svg{display:block}
.counter-band{left:0;top:389px;width:819px;height:43px;background:linear-gradient(var(--royal),#1747b3)}
.counter{left:70px;top:391px;color:#fff;font-size:32px;font-weight:700;letter-spacing:5px}
.counter-label{left:293px;top:409px;color:#fff;font-size:12px}
.dots{left:667px;top:405px;display:flex;gap:6px}
.dots i{width:10px;height:10px;border-radius:50%;background:#9aa0ad}
.dots i:first-child{background:#fff}

/* audience */
.mission{left:24px;top:457px;font-size:14.3px;color:var(--navy);font-weight:400}
.card{width:234px;height:149px;top:498px;border-radius:0 6px 0 0}
.card h3{position:absolute;left:0;right:0;top:20px;text-align:center;color:#fff;font-size:17px;font-weight:700}
.card .shot{position:absolute;left:33px;top:50px;width:190px;height:90px;border:2px solid #fff}
.c-dev{left:31px;background:linear-gradient(#3a3f90,var(--navy-deep))}
.c-team{left:298px;background:linear-gradient(#3a78e0,var(--royal))}
.c-exec{left:568px;background:linear-gradient(#d8e9f9,#b9d7f2)}
.c-exec h3{color:#fff;opacity:.9}
.badge{width:58px;height:58px;border-radius:50%;background:var(--navy);border:3px solid #e9edf8;box-shadow:0 0 0 2px var(--navy);top:492px}
.blurb{width:230px;font-size:9px;line-height:12.5px;top:658px}
.rule{height:1px;background:var(--line);top:743px}
.more-btn{width:59px;height:16px;border-radius:8px;background:linear-gradient(#3f6fd6,#163d9e);color:#fff;font-size:7px;line-height:16px;text-align:center;top:735px}

/* integrations */
.section-title{font-size:18px;color:var(--navy-deep);top:800px;font-weight:400}
.carousel{left:34px;top:845px;width:494px;height:90px;background:#f1f1f1}
.tile{top:857px;width:99px;height:66px;background:#fff;border:1px solid #d5d5d5}
.tile span{position:absolute;left:14px;top:7px;width:81px;height:52px;background:linear-gradient(90deg,#f3f3f3,#dcdcdc)}
.nudge{top:880px;width:9px;height:20px;background:#444;border-radius:2px}
.tech-shot{left:570px;top:848px;width:98px;height:61px;background:linear-gradient(135deg,#1d3f7a,#3aa0e6 55%,#9fd6f7)}
.tech-copy{left:681px;top:861px;width:118px;font-size:9px;line-height:12.5px}

/* footer */
.site-footer{left:0;top:979px;width:819px;height:221px;background:linear-gradient(#c8c8c8 0,#e6e6e6 4px,#dadada 100%)}
.f-title{font-size:18px;color:var(--navy-deep);top:1003px;font-weight:400}
.news-more{left:197px;top:1007px;width:43px;height:16px;border-radius:8px;background:#666;color:#fff;font-size:7px;line-height:16px;text-align:center}
.news-item{left:31px;width:209px;height:46px;background:#ececec;font-size:9px;line-height:12px;padding:11px 9px}
.byline{left:186px;font-size:9px;color:var(--grey)}
.vline{width:1px;background:#bbb;top:1003px;height:175px}
.links{font-size:8.3px;color:var(--navy);line-height:19.2px;font-weight:600}
.contact{left:576px;top:1042px;font-size:9px;line-height:13px;color:#111}
.social{top:1007px;width:20px;height:20px;border-radius:3px;background:#3b6ab8}
.map{left:699px;top:1048px;width:104px;height:77px;border:1px solid #bbb;background:linear-gradient(135deg,#f2efe6,#e1dccd)}
.copyright{left:576px;top:1170px;font-size:9px;color:var(--navy)}
</style>
</head>
<body>

<header class="abs site-header"></header>
<div class="abs brand header-brand"><span class="brand-mark"></span>ternvantage</div>
<div class="abs tagline">better software,<b>less sweat</b></div>
<div class="abs free">free ➘</div>
<div class="abs cta">GET STARTED</div>

<nav class="abs main-nav">
  <a href="#">Home</a>
  <a href="#" class="drop">About Us</a>
  <a href="#" class="drop active">Product</a>
  <a href="#">Plans &amp; Pricing</a>
  <a href="#">Blog</a>
  <a href="#">Contact Us</a>
</nav>
<div class="abs sign-in">SIGN IN</div>

<section class="abs hero"></section>
<div class="abs hero-photo" role="img" aria-label="Developer typing at a keyboard in front of a translucent screen of code"></div>
<p class="abs hero-copy">The only Keystroke Yield Metrics™ that accurately monitors Coding Effort in software development providing timely guidance for better quality releases and faster time to market.</p>
<div class="abs arrow" style="left:28px;top:224px"><svg width="34" height="34"><path d="M20 10 L12 17 L20 24" stroke="#fff" stroke-width="4" fill="none"/></svg></div>
<div class="abs arrow" style="left:763px;top:224px"><svg width="34" height="34"><path d="M14 10 L22 17 L14 24" stroke="#fff" stroke-width="4" fill="none"/></svg></div>

<div class="abs counter-band"></div>
<div class="abs counter">1,001,357</div>
<div class="abs counter-label">SOURCE CODE INTERACTIONS BENCHMARKED</div>
<div class="abs dots"><i></i><i></i><i></i><i></i><i></i></div>

<h2 class="abs mission">EMPOWER DEVELOPERS AND THEIR COMPANIES TO CREATE BETTER SOFTWARE, FASTER AND WITH LESS SWEAT!</h2>

<div class="abs card c-dev"><h3>DEVELOPERS</h3><div class="shot" style="background:linear-gradient(90deg,#fafafa,#d9dde6)" role="img" aria-label="Developer sketching a flow diagram on glass"></div></div>
<div class="abs card c-team"><h3>TEAM LEADERS</h3><div class="shot" style="background:linear-gradient(90deg,#e9eef5,#b9c7da)" role="img" aria-label="Team leader reviewing a laptop with colleagues"></div></div>
<div class="abs card c-exec"><h3>EXECUTIVES</h3><div class="shot" style="background:linear-gradient(90deg,#cfd6df,#5d6878)" role="img" aria-label="Executive signing documents at a desk"></div></div>
<div class="abs badge" style="left:8px"></div>
<div class="abs badge" style="left:275px"></div>
<div class="abs badge" style="left:545px"></div>

<p class="abs blurb" style="left:39px">I’m a paragraph. Click here to add your own text and edit me. I’m a great place for you to tell a story and let your users know a little more about you.</p>
<p class="abs blurb" style="left:305px">I’m a paragraph. Click here to add your own text and edit me. I’m a great place for you to tell a story and let your users know a little more about you.</p>
<p class="abs blurb" style="left:576px">I’m a paragraph. Click here to add your own text and edit me. I’m a great place for you to tell a story and let your users know a little more about you.</p>
<div class="abs rule" style="left:33px;width:230px"></div>
<div class="abs rule" style="left:298px;width:230px"></div>
<div class="abs rule" style="left:568px;width:230px"></div>
<div class="abs more-btn" style="left:202px">read more ▸</div>
<div class="abs more-btn" style="left:467px">read more ▸</div>
<div class="abs more-btn" style="left:740px">read more ▸</div>

<h2 class="abs section-title" style="left:40px">FEATURED&nbsp; INTEGRATIONS</h2>
<div class="abs carousel"></div>
<div class="abs tile" style="left:60px"><span role="img" aria-label="Team collaboration icon"></span></div>
<div class="abs tile" style="left:174px"><span role="img" aria-label="Chat and messaging icon"></span></div>
<div class="abs tile" style="left:286px"><span role="img" aria-label="Media and notes icon"></span></div>
<div class="abs tile" style="left:400px"><span role="img" aria-label="Keyboard icon"></span></div>
<div class="abs nudge" style="left:33px"></div>
<div class="abs nudge" style="left:520px"></div>

<h2 class="abs section-title" style="left:571px">TECHNOLOGY</h2>
<div class="abs tech-shot" role="img" aria-label="Hand touching a network of glowing technology icons"></div>
<p class="abs tech-copy">I’m a paragraph. Click here to add your own text and edit me. I’m a great</p>
<div class="abs rule" style="left:568px;width:230px;top:936px"></div>
<div class="abs more-btn" style="left:740px;top:928px">read more ▸</div>

<footer class="abs site-footer"></footer>
<svg class="abs" style="left:36px;top:995px" width="30" height="34" viewBox="0 0 30 34"><rect x="1" y="4" width="28" height="29" fill="#fff" stroke="#333"/><rect x="1" y="4" width="28" height="7" fill="#2f6fd0"/><text x="15" y="29" font-size="15" text-anchor="middle" font-family="Open Sans,sans-serif" fill="#111">14</text></svg>
<h3 class="abs f-title" style="left:78px">NEWS</h3>
<div class="abs news-more">more ▸</div>
<p class="abs news-item" style="top:1043px">I’m a paragraph. Click here to add your own text and edit me. I’m a great place for you</p>
<div class="abs byline" style="top:1092px">by admin</div>
<div class="abs rule" style="left:31px;width:209px;top:1111px;background:#bbb"></div>
<p class="abs news-item" style="top:1133px">I’m a paragraph. Click here to add your own text and edit me. I’m a great place for you</p>
<div class="abs byline" style="top:1180px">by admin</div>

<div class="abs vline" style="left:267px"></div>
<svg class="abs" style="left:293px;top:1000px" width="30" height="30" viewBox="0 0 30 30"><rect x="3" y="11" width="15" height="9" rx="4.5" transform="rotate(-45 10 15)" fill="none" stroke="#111" stroke-width="3"/><rect x="12" y="10" width="15" height="9" rx="4.5" transform="rotate(-45 20 15)" fill="none" stroke="#111" stroke-width="3"/></svg>
<h3 class="abs f-title" style="left:332px">LINKS</h3>
<div class="abs links" style="left:291px;top:1040px">HOME<br>PRODUC<br>ABOUT &amp; TECHNOLOGY<br>PLANS &amp; PRICING<br>FEATURED INTEGRATIONS<br>BLOG</div>
<div class="abs links" style="left:443px;top:1040px">PLANNING<br>CODING<br>QUALITY<br>PRODUCTION<br>OUTSOURCING</div>

<div class="abs vline" style="left:551px"></div>
<div class="abs brand" style="left:576px;top:1002px;font-size:18px"><span class="brand-mark" style="width:17px;height:17px"></span>ternvantage</div>
<div class="abs social" style="left:729px"></div>
<div class="abs social" style="left:754px"></div>
<div class="abs social" style="left:779px"></div>
<p class="abs contact">Level 1 (Marlow reception),<br>12 Quill Lane, Eastbury,<br>QL4 2ZX<br><br>Tel: +44 2070 000 111<br>&nbsp;Fax: +44 8700 000 222</p>
<div class="abs map" role="img" aria-label="Street map showing the office location"></div>
<div class="abs copyright">Copyright © 2013. All rights reserved.</div>

</body>
</html>
```